" A empresa tem como principal atrativo a grande variedade de joias infantis. Nosso maior diferencial são as peças de alta joalheria para crianças e a confecção de joias exclusivas e personalizadas para o publico de todas as idades. Temos um atelier para atendimento com hora marcada e o e-commerce é nossa principal vitrine. É possível conhecer algumas peças e parte da identidade da marca no nosso site www.brilhomirim.com.br e no instagram @brilhomirim "

```html
<!DOCTYPE html>
<html lang="pt-BR">
<head>
<meta charset="utf-8">
<title>Brilho Mirim — Envelope</title>
<link rel="stylesheet" href="https://fonts.googleapis.com/css2?family=Cinzel:wght@400&family=Great+Vibes&family=Open+Sans:wght@400&display=swap">
<style>
  :root {
    --backdrop: #f3f1ee;
    --paper-blue: #c0e2f4;
    --paper-white: #ffffff;
    --rule-grey: #a7abae;
    --brand-blue: #5aa7cd;
    --ink-grey: #7d8f99;
    --ornament-tint: #d8edf8;
  }
  html, body {
    margin: 0;
    width: 1200px;
    height: 1200px;
    overflow: hidden;
    background: var(--backdrop);
  }
  .envelope-sheet {
    display: block;
    width: 1200px;
    height: 1200px;
  }
  .paper { fill: var(--paper-blue); }
  .address-band { fill: var(--paper-white); }
  .band-rule { fill: var(--rule-grey); }
  .brand-mark { fill: none; stroke: var(--brand-blue); stroke-width: 1.4; }
  .brand-name {
    font-family: "Cinzel", serif;
    font-size: 10px;
    fill: var(--brand-blue);
    letter-spacing: 0.4px;
  }
  .brand-tagline {
    font-family: "Great Vibes", cursive;
    font-size: 6.5px;
    fill: var(--brand-blue);
  }
  .contact-line {
    font-family: "Open Sans", sans-serif;
    font-size: 3.1px;
    fill: var(--ink-grey);
  }
  .glow-inner { stop-color: var(--ornament-tint); }
  .glow-outer { stop-color: var(--paper-blue); }
  .bow-area { fill: url(#bowGlow); }
</style>
</head>
<body>
<svg class="envelope-sheet" viewBox="0 0 500 500" xmlns="http://www.w3.org/2000/svg">
  <defs>
    <radialGradient id="bowGlow" cx="50%" cy="45%" r="55%">
      <stop offset="0%" class="glow-inner"/>
      <stop offset="100%" class="glow-outer"/>
    </radialGradient>
    <clipPath id="bottomPanelClip">
      <polygon points="105,280 390,280 390,402 248,372 105,403"/>
    </clipPath>
  </defs>

  <!-- top flap -->
  <polygon class="paper" points="105,122 248,93 395,120 390,157 105,157"/>
  <!-- side flaps -->
  <polygon class="paper" points="83,160 105,150 105,282 88,272"/>
  <polygon class="paper" points="390,150 412,162 408,270 390,282"/>
  <!-- bottom panel -->
  <polygon class="paper" points="105,280 390,280 390,402 248,372 105,403"/>

  <!-- decorative bow, kept inside the bottom panel -->
  <g clip-path="url(#bottomPanelClip)">
    <rect class="bow-area" x="268" y="282" width="122" height="120" role="img" aria-label="Faint line drawing of a large ribbon bow"/>
  </g>

  <!-- address band -->
  <rect class="address-band" x="105" y="156" width="285" height="126"/>
  <rect class="band-rule" x="105" y="154" width="285" height="4"/>
  <rect class="band-rule" x="105" y="279" width="285" height="3"/>

  <!-- brand block -->
  <g class="brand">
    <circle class="brand-mark" cx="157" cy="181" r="7"/>
    <text class="brand-name" x="157" y="203" text-anchor="middle">BRILHO MIRIM</text>
    <text class="brand-tagline" x="157" y="212" text-anchor="middle">Doces joias com amor</text>
  </g>

  <!-- contact -->
  <g class="contact">
    <text class="contact-line" x="167" y="299" text-anchor="middle">www.brilhomirim.com.br · @brilhomirim</text>
    <text class="contact-line" x="170" y="306" text-anchor="middle">(11) 0000-0000 | (11) 90000-0000</text>
    <text class="contact-line" x="166" y="313" text-anchor="middle">Rua das Flores, 100 · São Paulo</text>
  </g>
</svg>
</body>
</html>
```